Bright Ridge Heating and Cooling inc

Free System Replacement estimate
Financing available
Indoor Air Quality
high efficiency system
Yarvo, Pictoloom, Chatterlane
website info
Se Habla Espanol
Free second opinion
We service all major brand

Target Market(s)

Hvac Home Services

Industry/Entity Type

Hvac

Font styles to use
Sans Serif
Other font styles liked:
• Tesla letter

Colors
3377b5
9bcb3c

```html
<!DOCTYPE html>
<html lang="en">
<head>
<meta charset="utf-8">
<title>Bright Ridge Heating and Cooling inc – Postcard</title>
<link href="https://fonts.googleapis.com/css2?family=Roboto+Condensed:ital,wght@0,300;0,400;0,700;0,900;1,700;1,900&family=Roboto:wght@900&display=swap" rel="stylesheet">
<style>
:root{
  --bg:#333333;
  --navy:#1c4478;
  --blue:#2f5d93;
  --green:#7cbc3f;
  --green-dark:#3e8a6c;
  --white:#ffffff;
  --badge:#1b2a44;
  --line:#555555;
}
*{margin:0;padding:0;box-sizing:border-box}
html,body{width:748px;height:1200px;overflow:hidden;background:var(--bg)}
body{position:relative;font-family:"Roboto Condensed",Arial,sans-serif;color:var(--white)}
.card{position:absolute;left:128px;width:492px;height:338px;overflow:hidden;background:var(--white)}
.card--front{top:31px}
.card--back{top:394px}
.card__bg{position:absolute;inset:0;width:492px;height:338px}
.abs{position:absolute}

/* logo */
.brand{position:absolute;left:318px;top:28px;display:flex;align-items:center;gap:7px;color:var(--navy);font-weight:900}
.brand__dot{width:26px;height:26px;border-radius:50%;background:var(--green)}
.brand__name{font-size:23px;line-height:22px;letter-spacing:.2px}
.brand__sub{display:block;font-size:9.5px;line-height:12px;letter-spacing:.3px}

/* front */
.tagline{left:23px;top:21px;font-size:7.6px;font-weight:700;letter-spacing:2.4px;white-space:nowrap}
.headline{left:22px;top:33px;font-family:"Roboto",Arial,sans-serif;font-weight:900;color:var(--navy);line-height:1;white-space:nowrap}
.headline__l1{display:block;font-size:30px;letter-spacing:-.4px}
.headline__l2{display:block;font-size:22.5px;margin-top:3px;letter-spacing:-.4px}
.headline__l3{display:block;font-family:"Roboto Condensed",Arial,sans-serif;font-size:16.5px;color:var(--white);margin-top:3px}
.compare{left:8px;top:113px;width:184px;height:92px;display:flex;gap:2px;background:var(--white)}
.compare__side{flex:1;display:flex;flex-direction:column}
.compare__label{height:17px;background:var(--navy);font-weight:700;font-size:11px;text-align:center;line-height:17px}
.compare__photo{flex:1}
.compare__photo--before{background:linear-gradient(160deg,#7e8f6a,#4f6b34 55%,#3d5a2a)}
.compare__photo--after{background:linear-gradient(160deg,#d9dcd9,#8e918f 50%,#a79a7e)}
.features{left:17px;top:223px;width:206px;display:grid;grid-template-columns:99px 107px;row-gap:4px;font-size:7.6px;font-weight:700;line-height:9px;list-style:none}
.features li{display:flex;gap:3px;white-space:nowrap}
.chev{color:var(--green);font-weight:900;font-size:9px;line-height:9px}
.phone-pill{left:12px;top:277px;width:209px;height:30px;border-radius:15px;background:var(--white);display:flex;align-items:center;gap:8px;padding-left:3px}
.phone-pill__icon{width:25px;height:25px;border-radius:50%;background:var(--green);display:flex;align-items:center;justify-content:center}
.phone-pill__num{font-family:"Roboto",Arial,sans-serif;font-weight:900;font-size:24px;color:var(--navy);letter-spacing:.2px}
.website{left:22px;top:310px;font-size:18.5px;font-weight:700}
.website__name{color:var(--green)}

/* back */
.story__kicker{left:26px;top:10px;font-size:15px;font-weight:300;letter-spacing:3px;color:var(--green)}
.story__title{left:26px;top:30px;font-size:18px;font-weight:300;line-height:1}
.story__title b{font-weight:700}
.story__rule{left:26px;top:51px;width:238px;height:1px;background:rgba(255,255,255,.6)}
.story__text{left:25px;top:61px;width:236px;font-size:8.3px;line-height:10.3px;font-weight:300}
.services__title{left:25px;top:165px;font-size:14px;font-weight:700;line-height:16px}
.services__divider{left:89px;top:166px;width:1px;height:30px;background:var(--white)}
.services__item{top:176px;font-size:8.8px;line-height:10.5px;display:flex;gap:4px}
.emergency__247{left:21px;top:209px;font-size:22px;font-weight:900;font-style:italic;letter-spacing:-1px}
.emergency__label{left:75px;top:210px;width:98px;height:12px;background:var(--white);color:var(--navy);font-size:10px;font-weight:900;font-style:italic;text-align:center;line-height:12px;transform:skewX(-12deg)}
.emergency__phone{left:70px;top:223px;width:100px;height:12px;border:1px solid var(--white);border-top:none;border-radius:0 0 6px 6px;font-size:9px;font-weight:700;display:flex;align-items:center;gap:4px;padding-left:8px}
.emergency__phone i{width:7px;height:7px;border-radius:50%;background:var(--green);display:inline-block}
.social{left:184px;top:219px;font-size:6px;font-weight:700;letter-spacing:.2px}
.badge-years{left:216px;top:236px;width:50px;height:50px;border-radius:50%;background:var(--badge);color:var(--white);text-align:center;font-size:9px;line-height:9.5px;padding-top:14px;font-weight:400}
.badge-years small{font-size:6.5px;display:block}
.address{left:312px;width:143px;height:1px;background:var(--line)}
</style>
</head>
<body>

<section class="card card--front" aria-label="Postcard front">
  <svg class="card__bg" viewBox="0 0 492 338">
    <defs>
      <linearGradient id="housePhoto" x1="0" y1="0" x2="0" y2="1">
        <stop offset="0" stop-color="#f1f2f2"/>
        <stop offset=".45" stop-color="#d5d8d8"/>
        <stop offset=".62" stop-color="#8d7764"/>
        <stop offset=".75" stop-color="#e9eaea"/>
        <stop offset="1" stop-color="#6f9b3c"/>
      </linearGradient>
    </defs>
    <rect x="0" y="0" width="492" height="216" fill="var(--green)"/>
    <rect x="0" y="216" width="492" height="122" fill="var(--blue)"/>
    <path d="M276 0 L492 0 L492 330 C330 318 232 290 222 230 C215 150 240 60 276 0 Z" fill="url(#housePhoto)" role="img" aria-label="Photo of an outdoor air conditioning unit beside a house with a service van on the lawn"/>
    <path d="M276 0 C240 60 215 150 222 230 C232 290 330 318 492 330" fill="none" stroke="var(--green)" stroke-width="6"/>
    <path d="M268 0 C232 60 207 150 214 230" fill="none" stroke="var(--navy)" stroke-width="2"/>
  </svg>

  <div class="brand">
    <span class="brand__dot"></span>
    <span class="brand__name">Bright Ridge<span class="brand__sub">Heating &amp; Cooling inc</span></span>
  </div>

  <p class="abs tagline">QUALITY THAT IS GUARANTED</p>
  <h1 class="abs headline">
    <span class="headline__l1">HEATING AND</span>
    <span class="headline__l2">AIR CONDITIONING</span>
    <span class="headline__l3">COMFORT SPECIALIST</span>
  </h1>

  <div class="abs compare">
    <div class="compare__side">
      <div class="compare__label">Before</div>
      <div class="compare__photo compare__photo--before" role="img" aria-label="Old outdoor unit overgrown with weeds"></div>
    </div>
    <div class="compare__side">
      <div class="compare__label">After</div>
      <div class="compare__photo compare__photo--after" role="img" aria-label="New outdoor unit on a clean pad"></div>
    </div>
  </div>

  <ul class="abs features">
    <li><span class="chev">»</span><span>Indoor Air Quality</span></li>
    <li><span class="chev">»</span><span>Financing available</span></li>
    <li><span class="chev">»</span><span>Free System<br>Replacement estimate</span></li>
    <li><span class="chev">»</span><span>Norvane Technologies high<br>efficiency on the background</span></li>
    <li><span class="chev">»</span><span>Se Habla Español</span></li>
    <li><span class="chev">»</span><span>Free second opinion</span></li>
  </ul>

  <div class="abs phone-pill">
    <span class="phone-pill__icon">
      <svg width="14" height="14" viewBox="0 0 24 24"><path d="M6.6 10.8c1.4 2.8 3.8 5.1 6.6 6.6l2.2-2.2c.3-.3.7-.4 1-.2 1.1.4 2.3.6 3.6.6.6 0 1 .4 1 1V20c0 .6-.4 1-1 1C10.6 21 3 13.4 3 4c0-.6.4-1 1-1h3.5c.6 0 1 .4 1 1 0 1.3.2 2.5.6 3.6.1.3 0 .7-.2 1l-2.3 2.2z" fill="#fff"/></svg>
    </span>
    <span class="phone-pill__num">555-014-0277</span>
  </div>

  <p class="abs website">www.<span class="website__name">brightridge365</span>.com</p>
</section>

<section class="card card--back" aria-label="Postcard back">
  <svg class="card__bg" viewBox="0 0 492 338">
    <defs>
      <clipPath id="panelClip">
        <path d="M0 0 L231 0 C270 60 300 130 290 210 C282 260 250 300 200 338 L0 338 Z"/>
      </clipPath>
      <linearGradient id="cityPhoto" x1="0" y1="0" x2="0" y2="1">
        <stop offset="0" stop-color="#9aa6c4"/>
        <stop offset=".35" stop-color="#c99c8a"/>
        <stop offset=".55" stop-color="#3b4b66"/>
        <stop offset="1" stop-color="#1f2c45"/>
      </linearGradient>
      <linearGradient id="wave" x1="0" y1="0" x2="1" y2="0">
        <stop offset="0" stop-color="var(--green)"/>
        <stop offset="1" stop-color="var(--green-dark)"/>
      </linearGradient>
    </defs>
    <rect width="492" height="338" fill="var(--white)"/>
    <path d="M190 338 C230 305 262 285 290 282 C360 276 430 312 492 338 Z" fill="url(#wave)"/>
    <g clip-path="url(#panelClip)">
      <rect width="492" height="338" fill="var(--blue)"/>
      <path d="M0 160 L140 160 L148 168 L492 168 L492 202 L0 202 Z" fill="var(--green)"/>
      <rect x="0" y="241" width="492" height="97" fill="url(#cityPhoto)" role="img" aria-label="Photo of a city skyline at dusk reflected in a lake"/>
    </g>
    <path d="M231 0 C270 60 300 130 290 210 C282 260 250 300 200 338" fill="none" stroke="var(--green)" stroke-width="4"/>
    <circle cx="175" cy="301" r="24" fill="#e6e6e6"/>
  </svg>

  <div class="brand">
    <span class="brand__dot"></span>
    <span class="brand__name">Bright Ridge<span class="brand__sub">Heating &amp; Cooling inc</span></span>
  </div>

  <p class="abs story__kicker">Our Story</p>
  <h2 class="abs story__title">MEET <b>BRIGHT RIDGE</b></h2>
  <div class="abs story__rule"></div>
  <p class="abs story__text">As a family owned and operated company, we take pride in the dedication of our HVAC services. We understand that time and cost are crucial, so we strive to go above and beyond our client's expectations. Our goal is to address every call promptly and with professionalism. Due to our fair rates, quality of work and outstanding services we have been able to help families meet their comfort needs. For our customers peace of mind, we offer valuable money saving service and maintenance contracts. Please call for additional details.</p>

  <p class="abs services__title">Our<br>Services</p>
  <div class="abs services__divider"></div>
  <p class="abs services__item" style="left:99px"><span>»</span><span>Annual<br>inspections</span></p>
  <p class="abs services__item" style="left:161px"><span>»</span><span>A/C<br>installation</span></p>
  <p class="abs services__item" style="left:224px"><span>»</span><span>Service<br>and repair</span></p>

  <p class="abs emergency__247">24/7</p>
  <p class="abs emergency__label">Emergency Service</p>
  <p class="abs emergency__phone"><i></i>555-014-0277</p>
  <p class="abs social">Chatterlane · Pictoloom · Yarvo</p>

  <div class="abs badge-years">11 YEARS<small>EXPERIENCE</small></div>

  <div class="abs address" style="top:116px"></div>
  <div class="abs address" style="top:163px"></div>
  <div class="abs address" style="top:211px"></div>
</section>

</body>
</html>
```